Business Card Design

New business card design

Target Market(s)

Residential & Commercial Property Managers

Industry/Entity Type

Plumbing Services

Contact Information for Business Card

Name - Owen Tredgold, title - Director, Phone Number - 0431 862 507, email - owen@rvb-plumbing.com.au, Company ABN - 73 215 904 386,

Font styles to use
Sans Serif

Colors
0054AA
0677BA
7BADD7
CADEEF
E8F1F8

```html
<!DOCTYPE html>
<html lang="en">
<head>
<meta charset="utf-8">
<title>RVB Plumbing Services – Business Card</title>
<link href="https://fonts.googleapis.com/css2?family=Poppins:wght@500;600;700&family=Source+Sans+3:wght@500&display=swap" rel="stylesheet">
<style>
  :root {
    --deep-blue: #0054AA;
    --mid-blue: #0677BA;
    --sky-blue: #7BADD7;
    --pale-blue: #CADEEF;
    --card-white: #EBF3FA;
    --splash-blue: #29A9E1;
    --ink: #1F1D22;
    --backdrop: #000000;
  }
  html, body {
    margin: 0;
    width: 1200px;
    height: 1200px;
    overflow: hidden;
    background: var(--backdrop);
  }
  .canvas {
    position: relative;
    width: 1200px;
    height: 1200px;
  }
  .card {
    position: absolute;
    left: 315px;
    width: 571px;
    height: 343px;
    border-radius: 44px;
    overflow: hidden;
  }
  .card-front {
    top: 254px;
    background: linear-gradient(90deg,
      #1656A8 0%, #2E68B2 12%, #5A8CC4 30%, #7BADD7 52%,
      #5A8CC4 64%, #2A66B3 82%, #1354A7 90%, #1354A7 100%);
  }
  .card-back {
    top: 617px;
    background: var(--card-white);
  }
  .brand-name {
    position: absolute;
    margin: 0;
    font-family: "Poppins", sans-serif;
    font-weight: 500;
    color: var(--ink);
    white-space: nowrap;
    line-height: 1;
    transform: translate(-50%, -50%);
  }
  .card-front .brand-name {
    left: 50%;
    top: 166px;
    font-size: 30px;
    letter-spacing: 1px;
  }
  .card-back .brand-name {
    left: 151px;
    top: 170px;
    font-size: 24px;
    letter-spacing: 0.5px;
  }
  .splash {
    position: absolute;
    inset: 0;
  }
  .divider {
    position: absolute;
    left: 284px;
    top: 87px;
    width: 3px;
    height: 169px;
    background: var(--ink);
  }
  .holder {
    position: absolute;
    left: 318px;
    top: 78px;
    font-family: "Poppins", sans-serif;
    color: var(--ink);
  }
  .holder-name {
    margin: 0;
    font-size: 27px;
    font-weight: 600;
    line-height: 1.1;
  }
  .holder-title {
    margin: 2px 0 0;
    font-size: 20px;
    font-weight: 500;
    line-height: 1.1;
  }
  .contact-list {
    position: absolute;
    left: 316px;
    top: 186px;
    margin: 0;
    padding: 0;
    list-style: none;
    font-family: "Source Sans 3", sans-serif;
    font-weight: 500;
    font-size: 14px;
    color: var(--ink);
  }
  .contact-list li {
    display: flex;
    align-items: center;
    gap: 8px;
    height: 20px;
  }
  .contact-list svg {
    width: 14px;
    height: 14px;
  }
  .abn {
    position: absolute;
    left: 0;
    right: 0;
    top: 294px;
    margin: 0;
    text-align: center;
    font-family: "Poppins", sans-serif;
    font-weight: 700;
    font-size: 20px;
    color: var(--ink);
    padding-right: 8px;
  }
</style>
</head>
<body>
<main class="canvas">
  <section class="card card-front" aria-label="Card front">
    <p class="brand-name">RVB Plumbing Services</p>
  </section>

  <section class="card card-back" aria-label="Card back">
    <svg class="splash" viewBox="0 0 571 343" aria-hidden="true">
      <path d="M0 0 H44 Q60 45 50 80 Q38 102 0 120 Z" fill="var(--splash-blue)"/>
      <path d="M571 207 Q520 270 521 300 Q522 325 541 343 H571 Z" fill="var(--splash-blue)"/>
    </svg>

    <p class="brand-name">RVB Plumbing</p>

    <div class="divider"></div>

    <div class="holder">
      <h1 class="holder-name">Owen Tredgold</h1>
      <p class="holder-title">Director</p>
    </div>

    <ul class="contact-list">
      <li>
        <svg viewBox="0 0 24 24" aria-hidden="true"><path fill="var(--ink)" d="M6.6 10.8c1.4 2.8 3.8 5.1 6.6 6.6l2.2-2.2c.3-.3.7-.4 1-.2 1.1.4 2.3.6 3.6.6.6 0 1 .4 1 1V20c0 .6-.4 1-1 1C10.6 21 3 13.4 3 4c0-.6.4-1 1-1h3.5c.6 0 1 .4 1 1 0 1.3.2 2.5.6 3.6.1.3 0 .7-.2 1z"/></svg>
        <span>0431 862 507</span>
      </li>
      <li>
        <svg viewBox="0 0 24 24" aria-hidden="true"><rect x="2" y="5" width="20" height="14" fill="none" stroke="var(--ink)" stroke-width="1.6"/><path d="M2 5l10 8 10-8M2 19l7.5-7M22 19l-7.5-7" fill="none" stroke="var(--ink)" stroke-width="1.6"/></svg>
        <span>owen@rvb-plumbing.com.au</span>
      </li>
    </ul>

    <p class="abn">COMPANY ABN – 73 215 904 386</p>
  </section>
</main>
</body>
</html>
```